Business cards & stationery for a cloth diaper retailer
Natural & Organic Baby Products
Bright & Fun-filled
Marisol Treveck
Carvale, MD 20843
info@dotsnugnest.com
www.dotsnugnest.com
My business is web-based so the website address needs to be highlighted on the card.
Services include:
- Cloth diapering workshops
- Newborn rental cloth diaper trial package
- Private In-Home Consults
- Office/Showroom hours

```html
<!DOCTYPE html>
<html lang="en">
<head>
<meta charset="utf-8">
<title>Dot's Snug Nest — Business Card</title>
<link rel="stylesheet" href="https://fonts.googleapis.com/css2?family=Nunito:wght@400;700;800&display=swap">
<style>
  :root {
    --green: #6cbf1c;
    --green-light: #9bd83a;
    --green-dark: #3f8f0e;
    --white: #ffffff;
    --ink: #4b4b4b;
    --backdrop: #eceae6;
    --art-skin: #f3d2b0;
    --art-leaf: #8acb3a;
  }
  * { box-sizing: border-box; margin: 0; padding: 0; }
  html, body { width: 1200px; height: 646px; overflow: hidden; }
  body {
    background: var(--backdrop);
    font-family: "Nunito", sans-serif;
    display: flex;
    align-items: center;
    justify-content: center;
    gap: 48px;
  }
  .card {
    position: relative;
    width: 540px;
    height: 309px;
    border-radius: 6px;
    overflow: hidden;
    box-shadow: 0 6px 18px rgba(0,0,0,.18);
  }
  /* Back side: services */
  .card-back {
    background: linear-gradient(135deg, var(--green-light), var(--green) 55%, var(--green-dark));
    color: var(--white);
  }
  .card-back .curve { position: absolute; inset: 0; }
  .services {
    position: absolute;
    left: 34px;
    top: 70px;
  }
  .services h2 {
    font-size: 22px;
    font-weight: 800;
    margin-bottom: 10px;
  }
  .services ul { list-style: none; }
  .services li {
    font-size: 13px;
    line-height: 1.7;
    padding-left: 14px;
    position: relative;
  }
  .services li::before {
    content: "";
    position: absolute;
    left: 0; top: 9px;
    width: 6px; height: 6px;
    border-radius: 50%;
    background: var(--white);
  }
  .back-web {
    position: absolute;
    left: 34px;
    bottom: 26px;
    font-size: 17px;
    font-weight: 800;
    letter-spacing: .5px;
  }
  .back-art {
    position: absolute;
    right: 40px;
    top: 22px;
    width: 190px;
    height: 170px;
    border-radius: 50%;
    background: radial-gradient(circle at 45% 40%, var(--art-skin), var(--art-leaf) 75%);
  }
  /* Front side: identity */
  .card-front { background: var(--white); }
  .card-front .panel { position: absolute; inset: 0; }
  .front-art-flowers {
    position: absolute;
    right: 150px;
    top: 18px;
    width: 90px;
    height: 70px;
    border-radius: 40%;
    background: radial-gradient(circle, #fffbe0, var(--art-leaf) 70%);
  }
  .person {
    position: absolute;
    left: 34px;
    top: 58px;
    font-size: 24px;
    font-weight: 800;
    color: var(--green);
  }
  .brand {
    position: absolute;
    left: 34px;
    bottom: 44px;
    display: flex;
    align-items: center;
    gap: 14px;
  }
  .brand-art {
    width: 76px;
    height: 76px;
    border-radius: 50%;
    background: radial-gradient(circle at 45% 40%, var(--art-skin), var(--art-leaf) 80%);
  }
  .brand-name {
    font-size: 26px;
    font-weight: 800;
    color: var(--green);
  }
  .contact {
    position: absolute;
    right: 24px;
    top: 96px;
    width: 150px;
    color: var(--white);
    font-size: 12px;
    line-height: 1.75;
    text-align: right;
  }
  .contact .web {
    font-weight: 800;
    font-size: 14px;
    margin-top: 6px;
  }
  .contact svg { width: 10px; height: 10px; vertical-align: -1px; margin-left: 4px; fill: var(--white); }
</style>
</head>
<body>

<section class="card card-back" aria-label="Card back: services">
  <svg class="curve" viewBox="0 0 540 309" aria-hidden="true">
    <path d="M540 0 L470 0 C510 90 520 200 470 309 L540 309 Z" fill="var(--white)"/>
  </svg>
  <div class="back-art" role="img" aria-label="Illustration of a cartoon baby holding a green vine"></div>
  <div class="services">
    <h2>Services</h2>
    <ul>
      <li>Cloth diapering workshops</li>
      <li>Private In-Home Consults</li>
      <li>Office/Showroom hours</li>
      <li>Newborn rental cloth diaper trial package</li>
    </ul>
  </div>
  <p class="back-web">www.dotsnugnest.com</p>
</section>

<section class="card card-front" aria-label="Card front: contact">
  <svg class="panel" viewBox="0 0 540 309" aria-hidden="true">
    <path d="M540 0 L300 0 C380 90 380 220 330 309 L540 309 Z" fill="var(--green)"/>
    <path d="M300 0 C380 90 380 220 330 309" fill="none" stroke="var(--green-dark)" stroke-width="3"/>
  </svg>
  <div class="front-art-flowers" role="img" aria-label="Illustration of white flowers on a green vine"></div>
  <p class="person">Marisol Treveck</p>
  <div class="brand">
    <div class="brand-art" role="img" aria-label="Illustration of a cartoon baby"></div>
    <span class="brand-name">Dot's Snug Nest</span>
  </div>
  <div class="contact">
    <p>Carvale, MD 20843</p>
    <p>301.555.0142<svg viewBox="0 0 10 10"><path d="M2 0h2l1 3-1.5 1a6 6 0 0 0 2.5 2.5L7 5l3 1v2c0 1-1 2-2 2A8 8 0 0 1 0 2c0-1 1-2 2-2z"/></svg></p>
    <p>301.555.0187<svg viewBox="0 0 10 10"><path d="M2 0h2l1 3-1.5 1a6 6 0 0 0 2.5 2.5L7 5l3 1v2c0 1-1 2-2 2A8 8 0 0 1 0 2c0-1 1-2 2-2z"/></svg></p>
    <p>marisoltrev</p>
    <p>info@dotsnugnest.com</p>
    <p class="web">www.dotsnugnest.com</p>
  </div>
</section>

</body>
</html>
```